Visitenkarten-Design für Catering/ Liefertouren
Vielen Dank für die professionelle Zusammenarbeit. Änderungen wurden schnell und treffend umgesetzt. Wir sind mit dem Ergebnis sehr zufrieden.
Zielgruppe
Catering/ Liefertouren für hochwertige selbstgemachte Quiches/ französische Tartes, Suppen, Currys
Aufgabenstellung
2 Visitenkarten im Format DIN6 (21x10,5) lang die sich auf der 1. (Bild) Seite unterscheiden aber mit identischer 2. Seite.
Karte 'Quiche' 1. Seite:
'Quiche '
Quiche Passion - depuis 2003
Quiches, Soups, Currys,
Catering, Abholung, Liefertouren
www.Kovendo.de,
info@kovendo.de
Karte 'Soups' 1. Seite:
'KovendoChicken, KovendoTofu'
2. Seite (für beide Karten identisch)
Seite soll eine Art Vorlage sein und besteht lediglich aus einer gestalterischen 'Umrahmung' und unserem Logo am unteren Seitenrand. Der Durchmesser des Logos soll max. 15% der gesamten Seitenlänge betragen.
Seite wird von uns mit Angeboten/ Aktionen bedruckt in kleiner Stückzahl nachträglich bedruckt.
1. Seiten (Quer- oder Hochformat je nach Bild möglich).
2. Seite im Hochformat.
Keine Vorgaben bzgl. Schrifttyp.

```html
<!DOCTYPE html>
<html lang="de">
<head>
<meta charset="utf-8">
<title>Kovendo – Visitenkarten</title>
<link rel="stylesheet" href="https://fonts.googleapis.com/css2?family=Crimson+Text:wght@400;600&display=swap">
<style>
  :root {
    --page-bg: #e6e6e6;
    --card-white: #ffffff;
    --ink-light: #ffffff;
    --brand-brown: #3b2320;
    --watermark: #f1f1f1;
    --band-dark: rgba(20, 28, 45, 0.45);
    --band-green: rgba(20, 30, 20, 0.45);
  }
  * { margin: 0; padding: 0; box-sizing: border-box; }
  html, body { width: 1200px; height: 767px; overflow: hidden; background: var(--page-bg); }
  body { position: relative; font-family: "Crimson Text", Georgia, serif; }

  .card { position: absolute; overflow: hidden; }
  .card--front { left: 68px; width: 662px; height: 331px; color: var(--ink-light); text-align: center; }
  .card--quiche { top: 40px; }
  .card--soups { top: 399px; }

  .card__photo { position: absolute; inset: 0; }
  .card--quiche .card__photo {
    background:
      radial-gradient(circle at 55% 40%, #8a6a3a 0%, #6b5a2e 22%, #4a4a2c 36%, #26334f 46%, #1f2c47 70%, #18223a 100%);
  }
  .card--soups .card__photo {
    background:
      radial-gradient(circle at 50% 55%, #9c3a1e 0%, #5a2a1c 18%, #2c3222 32%, transparent 45%),
      linear-gradient(90deg, #2f7a26 0%, #1f3d1c 25%, #232a26 50%, #2a4a1f 75%, #3f7a2a 100%);
  }

  .card__title {
    position: absolute; left: 0; right: 0;
    font-size: 64px; font-weight: 400; line-height: 1;
    text-shadow: 0 2px 6px rgba(0,0,0,0.4);
  }
  .card--quiche .card__title { top: 118px; }
  .card--soups .card__title { top: 42px; }

  .card__tagline { position: absolute; left: 0; right: 0; font-size: 14px; letter-spacing: 0.3px; }
  .card--quiche .card__tagline { top: 214px; left: 20px; }
  .card--soups .card__tagline { top: 209px; left: 14px; }

  .card__rule { position: absolute; height: 1px; width: 207px; background: var(--ink-light); }
  .card--quiche .card__rule { top: 241px; left: 244px; }
  .card--soups .card__rule { top: 237px; left: 232px; }

  .card__services { position: absolute; left: 0; right: 0; font-size: 17.5px; letter-spacing: 0.4px; text-shadow: 0 1px 3px rgba(0,0,0,0.5); }
  .card--quiche .card__services { top: 256px; left: -14px; }
  .card--soups .card__services { top: 250px; left: 12px; }
  .card__services .sep { margin: 0 3px; }

  .card__contact-band { position: absolute; left: 0; right: 0; bottom: 0; height: 41px; display: flex; justify-content: center; align-items: center; font-size: 13.5px; }
  .card--quiche .card__contact-band { background: var(--band-dark); }
  .card--soups .card__contact-band { background: var(--band-green); height: 44px; }
  .card__contact-band span { padding: 0 14px; line-height: 22px; }
  .card__contact-band span + span { border-left: 1px solid rgba(255,255,255,0.8); }

  .card--back { left: 810px; top: 40px; width: 335px; height: 658px; background: var(--card-white); }
  .card__frame { position: absolute; inset: 0; }
  .card__watermark {
    position: absolute; left: 0; right: 0; top: 250px;
    text-align: center; font-size: 74px; color: var(--watermark); line-height: 1;
  }
  .card__logo {
    position: absolute; left: 124px; top: 527px; width: 100px; height: 100px;
    border-radius: 50%; background: var(--brand-brown);
    display: flex; align-items: center; justify-content: center;
    color: var(--ink-light); font-size: 20px;
  }
</style>
</head>
<body>

<section class="card card--front card--quiche">
  <div class="card__photo" role="img" aria-label="Foto: Spinat-Quiche auf Gitterrost mit frischen Spinatblättern auf dunklem Schiefer"></div>
  <h1 class="card__title">Quiche</h1>
  <p class="card__tagline">Quiche Passion - depuis 2003</p>
  <div class="card__rule"></div>
  <p class="card__services">Quiches<span class="sep">|</span>Soups<span class="sep">|</span>Currys<span class="sep">|</span>Catering<span class="sep">|</span>Abholung<span class="sep">|</span>Liefertouren</p>
  <div class="card__contact-band">
    <span>www.Kovendo.de</span><span>+49 (0) 89-1234 5678</span><span>info@kovendo.de</span>
  </div>
</section>

<section class="card card--front card--soups">
  <div class="card__photo" role="img" aria-label="Foto: Tomatensuppe mit Croûtons im Gusstopf, umgeben von Kräutern, Paprika und Gewürzen"></div>
  <h1 class="card__title">Soups</h1>
  <p class="card__tagline">Quiche Passion - depuis 2003</p>
  <div class="card__rule"></div>
  <p class="card__services">Quiches<span class="sep">|</span>Soups<span class="sep">|</span>Currys<span class="sep">|</span>Catering<span class="sep">|</span>Abholung<span class="sep">|</span>Liefertouren</p>
  <div class="card__contact-band">
    <span>www.Kovendo.de</span><span>+49 (0) 89-1234 5678</span><span>info@kovendo.de</span>
  </div>
</section>

<section class="card card--back">
  <svg class="card__frame" width="335" height="658" viewBox="0 0 335 658" aria-hidden="true">
    <path d="M124 583 C110 580 96 580 84 586 C70 593 55 600 38 596 C30 594 24 590 19 585 V30 Q19 16 33 16 H302 Q316 16 316 30 V585 C311 590 305 594 297 596 C280 600 265 593 251 586 C239 580 225 580 211 583"
          fill="none" stroke="var(--brand-brown)" stroke-width="1.6"/>
  </svg>
  <div class="card__watermark">Kovendo</div>
  <div class="card__logo">Kovendo</div>
</section>

</body>
</html>
```